Dog themed post card for homeowners that may be willing to sell their house.

We will be sending these postcards to homeowners that may be interested in selling their house. Our business is themed around our dog "Biscuit"- Biscuit Gets Homes. We are using her as the focal point of the business because typically these homeowners get lots of mailers that are similar and we would like stand out with an inviting puppy dog.
We would like to included the icon for Chirpbook and Snapgrid with her handle "@BiscuitGetsHomes" and her website BiscuitGetsHomes-example.com and our phone number 555-482-1976.
We will be sending these postcards in batches to various subdivisions. For that reason please consider a format that can easily change the name of the subdivision. We are including the subdivision name because we want the postcard to be slightly more personal/targeted.
Our business is just starting and we would like to get some brand recognition going. We envision Biscuit Gets Homes predominately displayed somehow.
I have attached numerous pictures of Biscuit. We envision using one on each side of the postcard. Below are phrases we would like to include on the postcard in a format that you see fitting. Please use the verbiage below and not what is sketched on the uploaded postcard. The below verbiage is the most up to date.
-I recently bought a house in (subdivision name) and would love to buy yours.
-Call my humans today so we can give you a no obligation offer
-No money out of your pocket
-Quick closing
-Any condition
-Can help with moving expenses

Target Market(s)

Home owners with equity in their house that may need to sell quickly. These are generally people that do not enjoy the buying/selling of real estate. It can sometimes be someone who has recently inherited a home and doesnt want to deal with the headache. Other times it may be someone going through a divorce or forclosure and want to sell their home quickly.

Industry/Entity Type

Direct Marketing

Requirements
Must have
• Happy and bright feel. This industry is saturated with less than ethical people and we are trying to convey a very clean, honest, straight forward and scam-free process.

```html
<!DOCTYPE html>
<html lang="en">
<head>
<meta charset="utf-8">
<title>Biscuit Gets Homes – Postcard</title>
<link href="https://fonts.googleapis.com/css2?family=Montserrat:wght@300;400;500;600;700;800&display=swap" rel="stylesheet">
<style>
  :root{
    --ink:#111111;
    --paper:#ffffff;
    --mist:#efefef;
    --plum:#211a2b;
    --backdrop:#c4c4c4;
    --stamp-line:#555555;
  }
  html,body{margin:0;padding:0;width:1200px;height:1200px;overflow:hidden;background:var(--backdrop);}
  body{position:relative;font-family:"Montserrat",sans-serif;color:var(--ink);}
  .postcard{
    position:absolute;left:244px;width:1195px;height:854px;
    background:var(--paper);overflow:hidden;
    transform:scale(0.6209);transform-origin:0 0;
  }
  .postcard--front{top:48px;}
  .postcard--back{top:610px;}
  .postcard__art{position:absolute;inset:0;width:1195px;height:854px;}
  .brand{position:absolute;left:48px;margin:0;line-height:1;}
  .brand__name{display:block;font-weight:800;letter-spacing:0.5px;}
  .brand__tag{display:block;font-weight:400;}
  .front .brand{top:112px;}
  .front .brand__name{font-size:78px;}
  .front .brand__tag{font-size:74px;margin-top:2px;}
  .back .brand{top:190px;}
  .back .brand__name{font-size:56px;}
  .back .brand__tag{font-size:56px;}
  .pitch{position:absolute;left:63px;top:348px;margin:0;line-height:1;}
  .pitch__lead{display:block;font-weight:300;font-size:40px;letter-spacing:0.5px;line-height:50px;}
  .pitch__place{display:block;font-weight:600;font-size:62px;margin-top:6px;}
  .pitch__close{display:block;font-weight:500;font-size:25px;margin-top:8px;}
  .contact{position:absolute;}
  .contact__phone{display:flex;align-items:center;gap:14px;font-weight:500;}
  .contact__row{display:flex;align-items:center;gap:12px;font-weight:500;font-size:21px;}
  .contact__dot{width:20px;height:20px;border-radius:50%;background:currentColor;display:inline-block;}
  .front .contact{left:560px;top:700px;padding-left:36px;border-left:5px solid var(--ink);}
  .front .contact__phone{font-size:42px;}
  .front .contact__row{margin-top:10px;}
  .back .offer{position:absolute;left:53px;top:362px;margin:0;color:var(--paper);font-weight:500;font-size:26px;line-height:34px;}
  .benefits{position:absolute;left:53px;top:497px;margin:0;padding:0;list-style:none;color:var(--paper);font-size:23px;font-weight:500;}
  .benefits li{display:flex;align-items:center;gap:22px;height:39px;}
  .benefits svg{width:24px;height:24px;}
  .back .contact{left:53px;top:735px;color:var(--paper);}
  .back .contact__phone{font-size:40px;}
  .back .contact__line{display:flex;align-items:center;margin-top:12px;}
  .back .contact__divider{width:3px;height:38px;background:var(--paper);margin:0 38px;}
  .stamp-box{position:absolute;left:973px;top:50px;width:170px;height:180px;border:1.5px solid var(--stamp-line);}
</style>
</head>
<body>

<section class="postcard postcard--front front">
  <svg class="postcard__art" viewBox="0 0 1195 854" aria-hidden="false">
    <defs>
      <linearGradient id="dogPhoto" x1="0" y1="0" x2="1" y2="1">
        <stop offset="0" stop-color="#dfe1dd"/>
        <stop offset="0.5" stop-color="#c9cbc8"/>
        <stop offset="1" stop-color="#b8bab6"/>
      </linearGradient>
      <linearGradient id="housePhoto" x1="0" y1="0" x2="1" y2="1">
        <stop offset="0" stop-color="#e7e8ea"/>
        <stop offset="1" stop-color="#c7cac9"/>
      </linearGradient>
    </defs>
    <polygon fill="var(--mist)" points="0,505 120,640 0,730"/>
    <polygon fill="var(--mist)" points="885,605 1195,395 1195,854 1118,854"/>
    <polygon fill="var(--ink)" points="205,0 330,0 815,580 1195,328 1195,370 772,645"/>
    <polygon fill="url(#dogPhoto)" role="img" aria-label="Photo of Biscuit the shaggy grey dog in a bandana sitting on a front walkway" points="330,0 1195,0 1195,328 815,580"/>
    <polygon fill="var(--ink)" points="0,88 600,88 782,290 0,290"/>
    <polygon fill="var(--paper)" points="0,88 588,88 758,276 0,276"/>
    <polygon fill="var(--ink)" points="0,728 232,580 472,854 0,854"/>
    <polygon fill="url(#housePhoto)" role="img" aria-label="Photo of a white brick house front with shuttered windows" points="0,768 222,626 442,854 0,854"/>
  </svg>

  <h1 class="brand"><span class="brand__name">BISCUIT</span><span class="brand__tag">GETS HOMES</span></h1>

  <p class="pitch">
    <span class="pitch__lead">I RECENTLY<br>BOUGHT A HOUSE IN</span>
    <span class="pitch__place">MAPLE HOLLOW</span>
    <span class="pitch__close">AND WOULD LOVE TO BUY YOURS</span>
  </p>

  <div class="contact">
    <div class="contact__phone">
      <svg width="34" height="34" viewBox="0 0 24 24"><circle cx="12" cy="12" r="12" fill="currentColor"/><path d="M8.2 6.2l1.9-.4 1.2 2.8-1.3 1c.6 1.4 1.6 2.4 3 3l1-1.3 2.8 1.2-.4 1.9c-4.6.4-8.6-3.6-8.2-8.2z" fill="#fff"/></svg>
      555-482-1976
    </div>
    <div class="contact__row"><span class="contact__dot"></span>BiscuitGetsHomes-example.com</div>
    <div class="contact__row"><span class="contact__dot"></span>@BiscuitGetsHomes</div>
  </div>
</section>

<section class="postcard postcard--back back">
  <svg class="postcard__art" viewBox="0 0 1195 854">
    <polygon fill="var(--mist)" points="0,0 85,0 110,28 0,110"/>
    <polygon fill="var(--plum)" points="0,170 180,33 300,170"/>
    <polygon fill="var(--plum)" role="img" aria-label="Dimmed photo of Biscuit in front of a house" points="0,326 446,326 902,854 0,854"/>
    <polygon fill="var(--ink)" points="0,312 575,312 592,327 0,327"/>
    <line x1="476" y1="200" x2="590" y2="325" stroke="var(--ink)" stroke-width="7"/>
  </svg>

  <div class="stamp-box" aria-label="Postage area"></div>

  <h2 class="brand"><span class="brand__name">BISCUIT</span><span class="brand__tag">GETS HOMES</span></h2>

  <p class="offer">CALL MY HUMANS TODAY<br>SO WE CAN GIVE YOU<br>A NO OBLIGATION OFFER</p>

  <ul class="benefits">
    <li><svg viewBox="0 0 24 24"><circle cx="12" cy="12" r="10" fill="none" stroke="#fff" stroke-width="1.5"/><path d="M7 12l4 4 8-9" fill="none" stroke="#fff" stroke-width="1.8"/></svg>No money out of your pocket</li>
    <li><svg viewBox="0 0 24 24"><circle cx="12" cy="12" r="10" fill="none" stroke="#fff" stroke-width="1.5"/><path d="M7 12l4 4 8-9" fill="none" stroke="#fff" stroke-width="1.8"/></svg>Quick closing</li>
    <li><svg viewBox="0 0 24 24"><circle cx="12" cy="12" r="10" fill="none" stroke="#fff" stroke-width="1.5"/><path d="M7 12l4 4 8-9" fill="none" stroke="#fff" stroke-width="1.8"/></svg>Any condition</li>
    <li><svg viewBox="0 0 24 24"><circle cx="12" cy="12" r="10" fill="none" stroke="#fff" stroke-width="1.5"/><path d="M7 12l4 4 8-9" fill="none" stroke="#fff" stroke-width="1.8"/></svg>Can help with moving expenses</li>
  </ul>

  <div class="contact">
    <div class="contact__phone">
      <svg width="32" height="32" viewBox="0 0 24 24"><circle cx="12" cy="12" r="12" fill="#fff"/><path d="M8.2 6.2l1.9-.4 1.2 2.8-1.3 1c.6 1.4 1.6 2.4 3 3l1-1.3 2.8 1.2-.4 1.9c-4.6.4-8.6-3.6-8.2-8.2z" fill="#211a2b"/></svg>
      555-482-1976
    </div>
    <div class="contact__line">
      <div class="contact__row"><span class="contact__dot"></span>BiscuitGetsHomes-example.com</div>
      <span class="contact__divider"></span>
      <div class="contact__row"><span class="contact__dot"></span>@BiscuitGetsHomes</div>
    </div>
  </div>
</section>

</body>
</html>
```